Uprising SaaS company needs an attractive business card design

We're an uprising SaaS company who's attempting to attack the rigid car (insurance) claims management market in Europe.
We want to our mighty base order management system, listen to our clients to connect the smart ideas to build something even mightier.
We primarily focus on helping our customers manage their customers' claims/orders and get them resolved as smoothly as possible.
We'd like the business card design to express technical innovation and the fact that we connect smart ideas, as our company slogan indicates.
Contact Information for Business Card
Name, position, website, email, mobile, business address
Font styles to use
Colors
Designer to choose colors to be used in the design.
Look and feel
Each slider illustrates characteristics of the customer's brand and the style your logo design should communicate.

```html
<!DOCTYPE html>
<html lang="en">
<head>
<meta charset="utf-8">
<title>nexavio business card</title>
<link rel="stylesheet" href="https://fonts.googleapis.com/css2?family=Poppins:wght@300;400&display=swap">
<style>
  :root {
    --page: #2d2d2e;
    --card-top: #1c1d1f;
    --card-bottom: #2c2e31;
    --cyan: #6fbfd3;
    --band-grey: #6b6b6d;
    --text-light: #e4e4e4;
    --text-soft: #d0d0d0;
    --mark-front: #5a5e63;
  }
  * { margin: 0; padding: 0; box-sizing: border-box; }
  html, body {
    width: 1200px; height: 1138px; overflow: hidden;
    background: var(--page);
    font-family: "Poppins", sans-serif;
  }
  .stage { position: relative; width: 1200px; height: 1138px; }

  .card {
    position: absolute;
    border-radius: 14px;
    overflow: hidden;
    background: linear-gradient(160deg, var(--card-top) 0%, var(--card-bottom) 100%);
  }
  .card--front { left: 272px; top: 184px; width: 622px; height: 376px; }
  .card--back  { left: 274px; top: 606px; width: 620px; height: 375px; }

  .wordmark {
    position: absolute;
    font-weight: 300;
    line-height: 1;
    letter-spacing: 1px;
    white-space: nowrap;
  }
  .card--front .wordmark {
    left: 0; right: 0; top: 130px;
    text-align: center;
    font-size: 104px;
    color: var(--mark-front);
  }
  .card--back .wordmark {
    left: 24px; top: 62px;
    font-size: 92px;
    color: var(--text-light);
  }

  .front-url {
    position: absolute; left: 0; right: 0; top: 318px;
    display: flex; justify-content: center; align-items: center; gap: 18px;
    font-size: 17px; font-weight: 300; color: var(--text-light);
  }
  .front-url .rule { width: 46px; height: 2px; background: var(--cyan); }

  .band { position: absolute; left: 0; bottom: 0; }

  .holder { position: absolute; left: 26px; top: 206px; }
  .holder__name { font-size: 30px; font-weight: 400; color: var(--cyan); line-height: 1.1; }
  .holder__role { font-size: 17px; font-weight: 300; color: var(--text-soft); margin-top: 2px; }

  .address {
    position: absolute; left: 26px; top: 292px;
    font-size: 17px; font-weight: 300; color: var(--text-soft); line-height: 24px;
  }

  .contacts { position: absolute; left: 348px; top: 216px; list-style: none; }
  .contacts li {
    display: flex; align-items: center; gap: 10px;
    height: 24px;
    font-size: 17px; font-weight: 300; color: var(--text-light);
  }
  .contacts svg { width: 14px; height: 14px; flex: none; }

  .slogan {
    position: absolute; left: 302px; right: 0; top: 339px;
    text-align: center;
    font-size: 17px; font-weight: 300; color: var(--text-light);
  }
</style>
</head>
<body>
<main class="stage">

  <section class="card card--front" aria-label="Card front">
    <div class="wordmark">nexavio</div>
    <div class="front-url">
      <span class="rule"></span>
      <span>https://nexavio.com</span>
      <span class="rule"></span>
    </div>
    <svg class="band" width="622" height="11" viewBox="0 0 622 11">
      <rect x="0" y="0" width="311" height="11" fill="var(--band-grey)"/>
      <rect x="311" y="0" width="311" height="11" fill="var(--cyan)"/>
    </svg>
  </section>

  <section class="card card--back" aria-label="Card back">
    <div class="wordmark">nexavio</div>

    <div class="holder">
      <div class="holder__name">Lukas Brenner</div>
      <div class="holder__role">Managing Director</div>
    </div>

    <div class="address">
      Lindenweg 18b<br>
      10115 Berlin, Germany
    </div>

    <ul class="contacts">
      <li>
        <svg viewBox="0 0 14 14" aria-hidden="true">
          <path d="M1 5 Q7 1 13 5 L11.5 6.5 L9.5 5.5 L9.5 4.5 Q7 3.8 4.5 4.5 L4.5 5.5 L2.5 6.5 Z" fill="var(--cyan)"/>
          <path d="M3.5 7 L10.5 7 L12 12 L2 12 Z" fill="var(--cyan)"/>
        </svg>
        <span>+49 170 5550142</span>
      </li>
      <li>
        <svg viewBox="0 0 14 14" aria-hidden="true">
          <rect x="1" y="3" width="12" height="8.5" fill="var(--cyan)"/>
          <path d="M1 3 L7 8 L13 3 M1 11.5 L5.5 7 M13 11.5 L8.5 7" stroke="#222" stroke-width="1" fill="none"/>
        </svg>
        <span>info@nexavio.com</span>
      </li>
      <li>
        <svg viewBox="0 0 14 14" aria-hidden="true">
          <circle cx="7" cy="7" r="5.8" fill="none" stroke="var(--cyan)" stroke-width="1.2"/>
          <ellipse cx="7" cy="7" rx="2.6" ry="5.8" fill="none" stroke="var(--cyan)" stroke-width="1"/>
          <path d="M1.2 7 H12.8 M2 4.2 H12 M2 9.8 H12" stroke="var(--cyan)" stroke-width="1"/>
        </svg>
        <span>https://nexavio.com</span>
      </li>
    </ul>

    <svg class="band" width="620" height="45" viewBox="0 0 620 45">
      <rect x="0" y="32" width="300" height="13" fill="var(--band-grey)"/>
      <polygon points="302,0 620,0 620,45 264,45" fill="var(--cyan)"/>
    </svg>
    <div class="slogan">Linking Bright Minds.</div>
  </section>

</main>
</body>
</html>
```